BRIGHTDESK - Remote Tech Support Site

We are looking for a new very responsive and simple website for our brand Brightdesk.com - a remote technical support company.

This company supports customers Globally in different countries throughout Eur/ North America / South America / Asia etc (please keep this in mind and integrate into the idea).

Its important to us that the design is very explanatory, the customer should easily be able to figure out that we provide computer support right away ... I like one page responsive type designs as well without a bunch of menu items

Here are some similar sites we like - but still looking for a unique design that fits out brand "brightdesk" - I have upload also some layouts i like (but the designs are not important just the layouts), youll see it includes consumer business etc which is important.

VOLM.COM - I love how clean it is - nice and white easy to see everything

PLUMWIRE247.COM - also nice the layout and responsive one page design makes it easy to use

corvalfix.com - similar to plumwire design as well - you can get the idea im looking for between the two

You will notice those examples are much different then the attachments I added - again this is more of an idea for possible layouts .. attached is also the logo - could inspire color scheme / blue white black etc

Target Market(s)

Home consumers without computer knowledge , older age 45-65, small medium business ... computer repair - slow computers

Industry/Entity Type

Computer Repair

Logo Text

Brightdesk

Coding

Coded - Design and coding required

Number of Pages Required

1 page

Font styles to use
Sans Serif
Other font styles liked:
• your choice responsive

Colors

Designer to choose colors to be used in the design.

Requirements
Must have
• Clean - responsive - professional design - the name says it all - brightdesk
• CALL TO ACTIONS FOR "Get Help Now!" / "Learn More" etc
Nice to have
• We are looking for a new very responsive and simple website for our brand Brightdesk.com - a remote technical support company.
• This company supports customers Globally in different countries throughout Eur/ North America / South America / Asia etc (please keep this in mind and integrate into the idea).
• Its important to us that the design is very explanatory, the customer should easily be able to figure out that we provide computer support right away ... I like one page responsive type designs as well without a bunch of menu items
• Here are some similar sites we like - but still looking for a unique design that fits out brand "brightdesk" - I have upload also some layouts i like (but the designs are not important just the layouts), youll see it includes consumer business etc which is important.
• VOLM.COM - I love how clean it is - nice and white easy to see everything
• PLUMWIRE247.COM - also nice the layout and responsive one page design makes it easy to use
• corvalfix.com - similar to plumwire design as well - you can get the idea im looking for between the two
Should not have
• dark, packed page - bad small font -

```html
<!DOCTYPE html>
<html lang="en">
<head>
<meta charset="utf-8">
<title>Brightdesk – Remote Tech Support</title>
<link rel="stylesheet" href="https://fonts.googleapis.com/css2?family=Ubuntu:wght@300;400;500;700&family=Open+Sans:wght@400;600;700&display=swap">
<style>
:root{
  --blue:#2b8cf0;
  --blue-dark:#1a6fd0;
  --teal:#17b3c8;
  --teal-dark:#0f97aa;
  --aqua:#c3f3f8;
  --ink:#222a33;
  --text:#555d66;
  --muted:#8a9199;
  --line:#e3e6ea;
  --navy:#0d1827;
  --red:#e02020;
  --white:#fff;
}
*{box-sizing:border-box;margin:0;padding:0}
html,body{width:1200px;height:4235px;overflow:hidden}
body{font-family:"Open Sans",Arial,sans-serif;color:var(--text);background:#fff;font-size:14px}
h1,h2,h3,.display{font-family:"Ubuntu",Arial,sans-serif}
section,header,footer{position:relative;width:1200px;overflow:hidden}
.btn{display:inline-block;background:var(--blue);color:#fff;font-family:"Ubuntu",sans-serif;font-weight:500;border-radius:24px;padding:12px 28px;font-size:16px;text-decoration:none}
.section-title{display:flex;align-items:center;justify-content:center;gap:10px;font-family:"Ubuntu",sans-serif;font-weight:500;font-size:17px;letter-spacing:.5px;color:var(--ink);text-transform:uppercase}
.section-title svg{width:26px;height:26px}

/* hero */
.hero{height:580px;background:linear-gradient(90deg,#4d5560 0%,#6f7883 38%,#a9b3bd 60%,#c9d3dc 100%)}
.hero-photo{position:absolute;right:0;top:0;width:760px;height:580px;background:radial-gradient(ellipse at 60% 45%,#5a7aa6 0%,#8fa6c1 35%,rgba(200,210,220,0) 70%)}
.topbar{position:absolute;top:0;left:0;width:1200px;height:78px;background:rgba(20,30,45,.55);display:flex;align-items:center;justify-content:space-between;padding:0 170px 0 160px}
.brand{display:flex;align-items:center;gap:10px;color:#fff;font-family:"Ubuntu",sans-serif;font-weight:500;font-size:30px}
.brand i{width:34px;height:34px;border-radius:50%;background:var(--blue);display:block}
.phone{display:flex;align-items:center;gap:10px;color:#fff;font-family:"Ubuntu",sans-serif;font-size:22px}
.hero-copy{position:absolute;left:160px;top:222px;color:#fff}
.hero-copy h1{font-weight:300;font-size:46px;line-height:54px}
.hero-copy p{font-size:15px;margin:8px 0 20px}
.slider-dots{position:absolute;bottom:16px;left:560px;display:flex;gap:8px}
.slider-dots span{width:22px;height:4px;background:rgba(255,255,255,.5)}
.slider-dots span:first-child{background:#fff}

/* trust */
.trust{height:282px;text-align:center;padding-top:58px}
.trust h2{font-weight:700;font-size:19px;color:var(--ink)}
.trust h3{font-weight:500;font-size:21px;color:var(--blue);margin-top:6px}
.badges{display:flex;justify-content:center;align-items:center;gap:90px;margin-top:36px}
.badge-bar{width:120px;height:36px;background:#2f3338;border-radius:4px}
.badge-seal{width:110px;height:110px;border-radius:50%;background:radial-gradient(circle,#f2cc55,#b88a18)}
.badge-lock{width:90px;height:100px;border-radius:16px;background:#c8161e}

/* how it works */
.how{height:408px;background:linear-gradient(135deg,#e7f3fd,#cfe6fb 50%,#e9f4fd)}
.how .section-title{margin-top:50px}
.steps{position:absolute;top:123px;left:226px;display:flex;gap:32px}
.step{width:231px;height:226px;background:var(--blue);color:#fff;text-align:center;padding:28px 18px 0;box-shadow:0 4px 12px rgba(30,100,180,.25)}
.step svg{width:46px;height:46px}
.step hr{width:28px;border:0;border-top:2px solid #fff;margin:12px auto}
.step h3{font-size:18px;font-weight:500}
.step p{font-size:11.5px;line-height:16px;margin-top:8px;opacity:.9}

/* features */
.features{height:565px}
.features .section-title{margin-top:48px}
.feature-grid{position:absolute;top:114px;left:170px;display:grid;grid-template-columns:repeat(4,212px);gap:14px}
.feature{height:184px;border:1px solid var(--line);text-align:center;padding:28px 16px 0;box-shadow:0 1px 4px rgba(0,0,0,.05)}
.feature svg{width:44px;height:44px}
.feature h3{font-size:14px;font-weight:500;color:var(--ink);margin:16px 0 6px}
.feature p{font-size:11.5px;line-height:16px}
.feature.active{background:#0a0a0a;border-color:#0a0a0a}
.feature.active h3,.feature.active p{color:#fff}

/* consult */
.consult{height:453px;background:linear-gradient(90deg,#3c3f43,#5f6368 40%,#2c2f33)}
.consult-copy{position:absolute;left:160px;top:130px;color:#fff;font-family:"Ubuntu",sans-serif}
.consult-copy p{font-size:19px;line-height:26px;margin-bottom:16px;width:260px}
.consult-copy .btn{padding:10px 26px;font-size:14px}
.consult-copy small{display:block;color:#6fb2ff;font-size:12px;margin:6px 0 0 30px}
.player{position:absolute;left:437px;top:29px;width:608px;height:367px;background:#111}
.player-screen{position:absolute;inset:0 0 38px 0;background:linear-gradient(160deg,#3b3a3f,#6b4a3a 55%,#2d2c31)}
.player-controls{position:absolute;left:0;right:0;bottom:0;height:38px;background:#1c1c1c;display:flex;align-items:center;gap:12px;padding:0 14px}
.player-track{flex:1;height:6px;background:#444;border-radius:3px}
.player-big{position:absolute;left:282px;top:146px;width:46px;height:46px}
.player-side{position:absolute;right:8px;top:10px;display:flex;flex-direction:column;gap:6px}
.player-side span{width:26px;height:26px;background:rgba(0,0,0,.6);border-radius:4px}

/* plans */
.plans{height:578px}
.plans .section-title{margin-top:58px}
.plan-row{position:absolute;top:135px;left:226px;display:flex;gap:32px}
.plan{position:relative;width:231px;height:345px;background:var(--aqua)}
.plan-head{height:170px;background:var(--teal);color:#fff;text-align:center;clip-path:polygon(0 0,100% 0,100% 72%,50% 100%,0 72%);padding-top:16px}
.plan-head h3{font-size:17px;font-weight:700;letter-spacing:.5px}
.price{font-family:"Ubuntu",sans-serif;font-size:40px;font-weight:300;margin-top:4px}
.price sup{font-size:18px}
.price small{font-size:12px}
.plan-head p{font-size:10.5px}
.plan ul{list-style:none;padding:14px 16px 0}
.plan li{font-size:11.5px;color:#33525a;display:flex;gap:6px;align-items:center;margin-bottom:12px}
.plan li::before{content:"";width:11px;height:11px;background:var(--teal);border-radius:2px}
.plan-plus{position:absolute;left:97px;bottom:-18px;width:36px;height:36px;border-radius:50%;background:var(--blue);color:#fff;text-align:center;line-height:36px;font-size:20px}
.plan-tag{position:absolute;top:-36px;left:16px;background:#2d3136;color:#fff;font-size:11px;padding:8px 14px;font-weight:600}
.disclaimer{position:absolute;top:530px;width:1200px;text-align:center;font-size:12px}
.disclaimer b{color:var(--red);font-weight:400}

/* testimonials */
.reviews{height:339px;background:linear-gradient(100deg,#f3f4f5,#e4e6e8 45%,#f5f5f6)}
.reviews .section-title{margin-top:60px}
.quote{position:absolute;top:140px;left:250px;width:700px;text-align:center;font-size:12.5px;line-height:20px}
.q-mark{position:absolute;font-size:40px;color:var(--blue);font-family:"Ubuntu",sans-serif}
.author{position:absolute;top:218px;width:1200px;text-align:center;font-size:12px;color:var(--ink)}
.review-dots{position:absolute;top:312px;left:584px;display:flex;gap:6px}
.review-dots span{width:7px;height:7px;border-radius:50%;background:#c5c9cd}
.review-dots span:first-child{background:var(--blue)}

/* about */
.about{height:382px;background:#f6f7f8}
.about-copy{position:absolute;left:161px;top:75px;width:330px}
.about-copy h2{font-family:"Ubuntu",sans-serif;font-weight:400;font-size:22px;color:var(--ink);line-height:26px}
.about-copy h2 span{display:block;color:var(--blue);font-size:32px;font-weight:300}
.about-copy p{font-size:12px;line-height:18px;margin-top:14px}
.about-copy .btn{margin-top:22px;padding:10px 26px;font-size:14px}
.about-photo{position:absolute;right:0;top:0;width:640px;height:382px;background:linear-gradient(90deg,rgba(246,247,248,1),#dfe5ea 30%,#b9c4ce 70%,#8e9aa6)}

/* map + form */
.contact{height:367px}
.map{position:absolute;inset:0;background:linear-gradient(135deg,#ece8e0,#dcdcd2 45%,#e7e2d8)}
.quick-form{position:absolute;left:748px;top:0;width:292px;height:367px;background:var(--blue);padding:34px 28px 0;color:#fff}
.quick-form h3{font-size:16px;font-weight:700;text-align:center;letter-spacing:.5px;margin-bottom:18px}
.field{display:flex;height:28px;margin-bottom:8px}
.field i{width:28px;background:#1f2a37}
.field span{flex:1;background:#fff;color:#999;font-size:11px;line-height:28px;padding-left:8px}
.field.tall{height:52px}
.submit{display:block;margin:14px auto 0;width:100px;height:30px;border-radius:15px;background:#1f2a37;color:#fff;text-align:center;line-height:30px;font-size:13px;font-weight:600}

/* footer */
.site-footer{height:281px;background:var(--navy);color:#a9b2bd;font-size:11px;line-height:17px}
.foot-col{position:absolute;top:42px}
.foot-col h4{color:var(--blue);font-family:"Ubuntu",sans-serif;font-size:16px;font-weight:500;margin-bottom:10px;height:20px}
.foot-col a{color:var(--blue);text-decoration:none}
.foot-col ul{list-style:none}
.foot-col li::before{content:"› "}
.socials{display:flex;gap:8px;margin-top:10px}
.socials span{width:28px;height:28px;background:var(--blue)}
.foot-bottom{position:absolute;left:0;right:0;bottom:0;height:58px;border-top:1px solid #1f2b3b;text-align:center;line-height:58px;font-size:11px}
.to-top{position:absolute;left:586px;top:-12px;width:28px;height:24px;background:var(--navy);border:1px solid #2c3a4d}
</style>
</head>
<body>

<header class="hero">
  <div class="hero-photo" role="img" aria-label="Smiling technician working on a laptop in a bright office"></div>
  <div class="topbar">
    <div class="brand"><i></i>brightdesk</div>
    <div class="phone">
      <svg width="22" height="22" viewBox="0 0 24 24" fill="none" stroke="#fff" stroke-width="2"><path d="M5 3h4l2 5-2.5 1.5a11 11 0 005 5L15 12l5 2v4a2 2 0 01-2 2A16 16 0 013 5a2 2 0 012-2z"/></svg>
      (800) 555-0142
    </div>
  </div>
  <div class="hero-copy">
    <h1>Dedicated Support<br>Anytime. Anywhere.</h1>
    <p>we have everything for your computer and internet security!</p>
    <a class="btn" href="#">Get Help Now!</a>
  </div>
  <div class="slider-dots"><span></span><span></span><span></span></div>
</header>

<section class="trust">
  <h2>Brightdesk is the most trusted services company</h2>
  <h3>Recognized By</h3>
  <div class="badges">
    <div class="badge-bar" role="img" aria-label="Review site badge"></div>
    <div class="badge-seal" role="img" aria-label="Satisfaction guarantee seal"></div>
    <div class="badge-lock" role="img" aria-label="Security certificate badge"></div>
  </div>
</section>

<section class="how">
  <div class="section-title">
    <svg viewBox="0 0 24 24" fill="none" stroke="#333" stroke-width="1.5"><rect x="3" y="3" width="18" height="14" rx="2"/><path d="M9 21h6M12 17v4M10 8a2 2 0 114 0c0 1.5-2 1.5-2 3"/></svg>
    How it works
  </div>
  <div class="steps">
    <div class="step">
      <svg viewBox="0 0 48 48" fill="none" stroke="#fff" stroke-width="2"><rect x="10" y="6" width="28" height="36" rx="2"/><path d="M18 6v4h12V6M16 26h4l3-6 4 10 3-4h4"/></svg>
      <hr><h3>Free Diagnostic</h3>
      <p>Get a diagnostic, FOR FREE! Get a free consultation with our staff.</p>
    </div>
    <div class="step">
      <svg viewBox="0 0 48 48" fill="none" stroke="#fff" stroke-width="2"><circle cx="24" cy="24" r="14"/><circle cx="24" cy="24" r="5"/><path d="M24 4v8M24 36v8M4 24h8M36 24h8"/></svg>
      <hr><h3>Get Fixed</h3>
      <p>Get fixed, IMMEDIATELY! Our staff will solve your computer issues right before your eyes.</p>
    </div>
    <div class="step">
      <svg viewBox="0 0 48 48" fill="none" stroke="#fff" stroke-width="2"><path d="M14 34h22a8 8 0 000-16 12 12 0 00-23 3 7 7 0 001 13z"/><path d="M24 22v12M19 27l5-5 5 5"/></svg>
      <hr><h3>Backup your Information!</h3>
      <p>Saving your files is now EASY! You will be able to retain your personal files without any loss of data.</p>
    </div>
  </div>
</section>

<section class="features">
  <div class="section-title">
    <svg viewBox="0 0 24 24" fill="none" stroke="#333" stroke-width="1.5"><path d="M4 20l9-9M14 4l6 6-3 3-6-6zM4 4l5 5M20 20l-5-5"/></svg>
    Our extreme features of services
  </div>
  <div class="feature-grid">
    <div class="feature active">
      <svg viewBox="0 0 44 44" fill="none" stroke="#fff" stroke-width="1.8"><circle cx="22" cy="22" r="15"/><path d="M11 11l22 22"/></svg>
      <h3>Ad Blocker</h3><p>Avoid unwanted Pop-ups with the newest Ad Blocking technology.</p>
    </div>
    <div class="feature">
      <svg viewBox="0 0 44 44" fill="none" stroke="var(--blue)" stroke-width="1.8"><rect x="10" y="8" width="24" height="28" rx="2"/><path d="M15 16h14M15 22h14M15 28h8"/></svg>
      <h3>Regular Tune-Ups</h3><p>Get a Regular Tune-Up and Optimization every 90 days.</p>
    </div>
    <div class="feature">
      <svg viewBox="0 0 44 44" fill="none" stroke="var(--blue)" stroke-width="1.8"><rect x="6" y="10" width="32" height="22" rx="2"/><path d="M10 22h6l3-6 4 10 3-4h8M16 38h12"/></svg>
      <h3>System Reports</h3><p>Stay up to date with Real-Time System Reporting.</p>
    </div>
    <div class="feature">
      <svg viewBox="0 0 44 44" fill="none" stroke="var(--blue)" stroke-width="1.8"><rect x="8" y="8" width="18" height="28" rx="2"/><rect x="24" y="16" width="12" height="20" rx="2"/></svg>
      <h3>Multiple Devices</h3><p>Get support for up to 6 multiple devices. Ask about our Family Plans.</p>
    </div>
    <div class="feature">
      <svg viewBox="0 0 44 44" fill="none" stroke="var(--blue)" stroke-width="1.8"><path d="M14 30c0-10 2-16 8-16s8 6 8 16M18 32c0-8 1-12 4-12s4 4 4 12M22 26v10M10 22c0-8 5-14 12-14s12 6 12 14"/></svg>
      <h3>Identity Protection</h3><p>Your details stay private with round-the-clock monitoring.</p>
    </div>
    <div class="feature">
      <svg viewBox="0 0 44 44" fill="none" stroke="var(--blue)" stroke-width="1.8"><rect x="13" y="6" width="18" height="32" rx="3"/><circle cx="22" cy="22" r="5"/></svg>
      <h3>Mobile Security</h3><p>Keep phones and tablets safe from threats and malware.</p>
    </div>
    <div class="feature">
      <svg viewBox="0 0 44 44" fill="none" stroke="var(--blue)" stroke-width="1.8"><rect x="6" y="10" width="24" height="18" rx="2"/><rect x="26" y="18" width="12" height="18" rx="2"/><path d="M12 34h12"/></svg>
      <h3>Cross Platform Support</h3><p>One Support Plan for different types of devices.</p>
    </div>
    <div class="feature">
      <svg viewBox="0 0 44 44" fill="none" stroke="var(--blue)" stroke-width="1.8"><path d="M12 30h20a7 7 0 000-14 10 10 0 00-19 3 6 6 0 00-1 11z"/><path d="M22 22v10M18 28l4 4 4-4"/></svg>
      <h3>Cloud Backup</h3><p>Keep your data safe! Ask about our plans for Unlimited Cloud Backup.</p>
    </div>
  </div>
</section>

<section class="consult" role="img" aria-label="Support agent wearing a headset in a call centre">
  <div class="consult-copy">
    <p>Get a 30-minute one-on-one free consultation with one of our experts! *</p>
    <p>And get started with our dedicated technicians.</p>
    <a class="btn" href="#">CALL US TODAY..!</a>
    <small>*Limited period offer</small>
  </div>
  <div class="player">
    <div class="player-screen" role="img" aria-label="Animated explainer video of a person at a desk"></div>
    <svg class="player-big" viewBox="0 0 46 46"><circle cx="23" cy="23" r="21" fill="none" stroke="#fff" stroke-width="3"/><path d="M18 14l14 9-14 9z" fill="#fff"/></svg>
    <div class="player-side"><span></span><span></span><span></span></div>
    <div class="player-controls">
      <svg width="14" height="14" viewBox="0 0 14 14"><path d="M2 1l11 6-11 6z" fill="#fff"/></svg>
      <div class="player-track"></div>
      <svg width="18" height="14" viewBox="0 0 18 14" fill="none" stroke="#fff" stroke-width="1.5"><path d="M2 2h5M2 2v5M16 12h-5M16 12V7"/></svg>
    </div>
  </div>
</section>

<section class="plans">
  <div class="section-title">
    <svg viewBox="0 0 24 24" fill="none" stroke="#333" stroke-width="1.5"><circle cx="12" cy="8" r="4"/><path d="M4 21c0-4 4-7 8-7s8 3 8 7"/></svg>
    Membership plans &amp; services
  </div>
  <div class="plan-row">
    <div class="plan">
      <div class="plan-head"><h3>PREMIUM</h3><div class="price"><sup>$</sup>19.99<small>/Mon</small></div><p>($149-$300 setup fee)</p></div>
      <ul><li>Regular 90-Day Optimization</li><li>Unlimited 24/7 Tier 1</li><li>Technician Support</li></ul>
      <div class="plan-plus">+</div>
    </div>
    <div class="plan">
      <div class="plan-head"><h3>PREMIUM PLUS</h3><div class="price"><sup>$</sup>29.99<small>/Mon</small></div><p>($149-$300 setup fee)</p></div>
      <ul><li>Regular 90-Day Optimization</li><li>Unlimited 24/7 Tier 3</li><li>Technician Support</li></ul>
      <div class="plan-plus">+</div>
    </div>
    <div class="plan">
      <div class="plan-tag">RECOMMENDED PLAN</div>
      <div class="plan-head"><h3>PLATINUM</h3><div class="price"><sup>$</sup>39.99<small>/Mon</small></div><p>($149-$300 setup fee)</p></div>
      <ul><li>Regular 90-Day Optimization</li><li>Unlimited 24/7 Tier 3</li><li>Technician Support</li><li>Online Identity Theft Protection</li></ul>
      <div class="plan-plus">+</div>
    </div>
  </div>
  <p class="disclaimer"><b>* Disclaimer</b> : FREE Optimization and Diagnostic when you call in. Limited time offer.</p>
</section>

<section class="reviews">
  <div class="section-title">
    <svg viewBox="0 0 24 24" fill="none" stroke="#333" stroke-width="1.5"><path d="M4 4h16v12H9l-5 4z"/><path d="M9 9h2v3M13 9h2v3"/></svg>
    What our customers said
  </div>
  <span class="q-mark" style="left:215px;top:128px">&ldquo;</span>
  <p class="quote">I contacted them about a serious threat on my laptop, they have completely transformed the laptop, it now functions like a brand new laptop, the staff were excellent, really patient and helpful, excellent service and would highly recommend, thank you.</p>
  <span class="q-mark" style="left:960px;top:165px">&rdquo;</span>
  <p class="author">- Martin Keller<br>UK</p>
  <div class="review-dots"><span></span><span></span><span></span></div>
</section>

<section class="about">
  <div class="about-photo" role="img" aria-label="Smiling support agent with headset at a computer"></div>
  <div class="about-copy">
    <h2>You Have to Know <span>ABOUT US</span></h2>
    <p>Our team is a leader in providing top notch quality services and products with a focus on our customer's needs. We are happy to discuss your computer issues and provide a free valuable diagnostic to determine the best solutions.</p>
    <p>While you are looking for the best source out there, we have everything for your computer and internet security!</p>
    <a class="btn" href="#">READ MORE</a>
  </div>
</section>

<section class="contact">
  <div class="map" role="img" aria-label="City street map showing the office location"></div>
  <form class="quick-form">
    <h3>GET QUICK HELP NOW</h3>
    <div class="field"><i></i><span>Name</span></div>
    <div class="field"><i></i><span>Email</span></div>
    <div class="field"><i></i><span>Phone No</span></div>
    <div class="field"><i></i><span>Subject</span></div>
    <div class="field tall"><i></i><span>Message</span></div>
    <span class="submit">Submit</span>
  </form>
</section>

<footer class="site-footer">
  <div class="foot-col" style="left:161px;width:150px">
    <h4>Contact us!</h4>
    <p>Canada Office<br>Northlane Ltd, 48 Maple Row,<br>Riverton, ON K0A 1Z0 Canada</p>
    <p style="margin-top:14px">Tel: (800) 555-0142</p>
    <p style="margin-top:14px">Email: <a href="#">info@brightdesk.com</a></p>
  </div>
  <div class="foot-col" style="left:330px;width:170px">
    <h4></h4>
    <p>United Kingdom Office<br>Northlane Ltd, 7 Fenwick Lane,<br>Ashbury AB1 2CD, UK</p>
    <p style="margin-top:14px">Tel: (800) 555-0142</p>
    <p style="margin-top:14px">Email: <a href="#">info@brightdesk.com</a></p>
  </div>
  <div class="foot-col" style="left:655px">
    <h4>Quick Links</h4>
    <ul><li>FAQ</li><li>Terms and Conditions</li><li>Refund Policy</li><li>Privacy Policy</li></ul>
  </div>
  <div class="foot-col" style="left:867px">
    <h4>Our Social Media!</h4>
    <p>Follow and get in touch us!</p>
    <div class="socials"><span></span><span></span></div>
  </div>
  <div class="foot-bottom">
    <span class="to-top"><svg width="26" height="22" viewBox="0 0 26 22"><path d="M8 13l5-5 5 5" fill="none" stroke="#a9b2bd" stroke-width="1.5"/></svg></span>
    © 2017 Brightdesk . All rights reserved.
  </div>
</footer>

</body>
</html>
```